Employee I.D. Card - Badge

We need an employee I.D. card designed. Our employees are going to be wearing these. I would like to have it look nice. Something professional yet cool (not uptight if that makes sense).
Project Scope:
Vertical orientation
Company name ------------- (Bright and Tidy)
Website ------------- (brightandtidymn.example)
Employee Picture
background check image
front and back designed - same design on either side
You can create the card without having the employee images on them.
Here are the dimensions -
2.125 x 3.370 inches
Double sided - same design can be used front and back
Background badge - I would like to add an image that shows that the employee has taken a background check. I've added the press-kit for the company we use. If you have a better idea than incorporating their logo, we can certainly do something different.
Example image-
https://www.findwell-search.example/results?q=background+check+badge&mode=images
The print company will set up the names.
Logo is attached
Also attached are our business cards. You can use this for an idea of brand/company style.
Our website - brightandtidymn.example

```html
<!DOCTYPE html>
<html lang="en">
<head>
<meta charset="utf-8">
<title>Bright and Tidy – Employee ID Card</title>
<link href="https://fonts.googleapis.com/css2?family=Roboto:wght@300;400;700&display=swap" rel="stylesheet">
<style>
  :root {
    --board: #808185;
    --white: #ffffff;
    --paper-top: #ffffff;
    --paper-bottom: #eef0f1;
    --brand-blue: #1a8fd8;
    --blue-deep: #0a6fbd;
    --blue-light: #1fa3e4;
    --green: #a8cc32;
    --green-light: #c3db2f;
    --yellow: #ebe713;
    --ink: #3a3a3a;
    --ink-soft: #2f4a3a;
    --seal: #d4a838;
    --seal-core: #2b2b2b;
    --photo-top: #3d5c78;
    --photo-bottom: #22384d;
  }
  * { margin: 0; padding: 0; box-sizing: border-box; }
  html, body {
    width: 1200px; height: 810px; overflow: hidden;
    background: var(--board);
    font-family: 'Roboto', sans-serif;
  }
  .board { position: relative; width: 1200px; height: 810px; }
  .id-card {
    position: absolute; top: 118px;
    width: 360px; height: 570px;
    box-shadow: 0 2px 6px rgba(0,0,0,0.25);
    overflow: hidden;
  }
  .id-card--front { left: 162px; }
  .id-card--back { left: 680px; }
  .card-bg { position: absolute; inset: 0; width: 100%; height: 100%; }
  .wordmark {
    position: absolute; left: 0; right: 0; text-align: center;
    font-weight: 400; letter-spacing: -0.5px; white-space: nowrap;
  }
  .id-card--front .wordmark { top: 60px; font-size: 32px; color: var(--brand-blue); }
  .id-card--back .wordmark { top: 160px; font-size: 42px; color: var(--white); }
  .employee-photo {
    position: absolute; left: 88px; top: 161px;
    width: 184px; height: 184px; border-radius: 50%;
    border: 3px solid var(--white);
    background: linear-gradient(180deg, var(--photo-top), var(--photo-bottom));
  }
  .employee-name {
    position: absolute; top: 368px; left: 0; right: 0; text-align: center;
    font-size: 20px; font-weight: 700; letter-spacing: 1px; color: var(--ink);
  }
  .employee-role {
    position: absolute; top: 397px; left: 0; right: 0; text-align: center;
    font-size: 17px; font-weight: 300; color: var(--white);
  }
  .check-seal {
    position: absolute; left: 138px; top: 437px;
    width: 84px; height: 84px; border-radius: 50%;
    background: var(--seal);
    box-shadow: 0 1px 3px rgba(0,0,0,0.25);
  }
  .check-seal::after {
    content: ""; position: absolute; inset: 12px; border-radius: 50%;
    background: var(--seal-core);
  }
  .tagline {
    position: absolute; top: 255px; left: 0; right: 0; text-align: center;
    font-size: 17px; font-weight: 300; color: var(--white); letter-spacing: 0.3px;
  }
  .website {
    position: absolute; top: 536px; left: 0; right: 0; text-align: center;
    font-size: 12.5px; font-weight: 400; letter-spacing: 0.4px;
  }
  .id-card--front .website { color: var(--white); }
  .id-card--back .website { color: var(--ink-soft); }
</style>
</head>
<body>
<main class="board">

  <section class="id-card id-card--front">
    <svg class="card-bg" viewBox="0 0 300 475" preserveAspectRatio="none" aria-hidden="true">
      <defs>
        <linearGradient id="paperFill" x1="0" y1="0" x2="0" y2="1">
          <stop offset="0" stop-color="var(--paper-top)"/>
          <stop offset="1" stop-color="var(--paper-bottom)"/>
        </linearGradient>
        <linearGradient id="frontGreen" x1="0" y1="0" x2="0" y2="1">
          <stop offset="0" stop-color="var(--green)"/>
          <stop offset="1" stop-color="var(--green-light)"/>
        </linearGradient>
      </defs>
      <rect width="300" height="475" fill="url(#paperFill)"/>
      <polygon points="0,182 150,262 300,182 300,475 0,475" fill="var(--blue-deep)"/>
      <polygon points="0,207 150,287 300,207 300,475 0,475" fill="url(#frontGreen)"/>
      <polygon points="0,340 150,420 300,340 300,475 0,475" fill="#ffffff" opacity="0.06"/>
    </svg>
    <div class="wordmark">Bright and Tidy</div>
    <div class="employee-photo" role="img" aria-label="Employee portrait photo"></div>
    <h2 class="employee-name">DANIEL WHITMORE</h2>
    <p class="employee-role">Accountant</p>
    <div class="check-seal" role="img" aria-label="Background check cleared seal"></div>
    <p class="website">brightandtidymn.example</p>
  </section>

  <section class="id-card id-card--back">
    <svg class="card-bg" viewBox="0 0 300 475" preserveAspectRatio="none" aria-hidden="true">
      <defs>
        <linearGradient id="backBlue" x1="0" y1="0" x2="0" y2="1">
          <stop offset="0" stop-color="var(--blue-deep)"/>
          <stop offset="1" stop-color="var(--blue-light)"/>
        </linearGradient>
        <linearGradient id="backGreen" x1="0" y1="0" x2="0" y2="1">
          <stop offset="0" stop-color="var(--green)"/>
          <stop offset="1" stop-color="var(--yellow)"/>
        </linearGradient>
      </defs>
      <rect width="300" height="475" fill="url(#backBlue)"/>
      <polygon points="0,282 150,334 300,282 300,475 0,475" fill="var(--white)"/>
      <polygon points="0,289 150,341 300,289 300,475 0,475" fill="url(#backGreen)"/>
      <polygon points="0,330 150,400 300,330 300,475 0,475" fill="#ffffff" opacity="0.06"/>
    </svg>
    <div class="wordmark">Bright and Tidy</div>
    <p class="tagline">Exterior Property Cleaning</p>
    <p class="website">brightandtidymn.example</p>
  </section>

</main>
</body>
</html>
```